I need the below text put into an illustration/high res image so I can print out and frame and give to my fiance. Can be simple but must look elegant. Idea is that the text can be written in the sand on the attached pics (let me know if you require more high res). Not precious on the dimensions but think no more than 90cm length or width. Can be smaller whatever you think works best. You can half long sentences if you think it will look better.
Update: some of you asked for a picture of us, not sure it works but have attached one
Marriage
Marriage isn’t for you.
You don’t marry to make yourself happy, you marry to make someone else happy.
More than that, your marriage isn’t for yourself, you’re marrying for a family.
Not just for the in-laws and all of that nonsense, but for your future children.
Who do you want to help you raise them?
Who do you want to influence them?
Marriage isn’t for you.
It’s not about you.
Marriage is about the person you married.

```html
<!DOCTYPE html>
<html lang="en">
<head>
<meta charset="utf-8">
<title>Marriage</title>
<link rel="stylesheet" href="https://fonts.googleapis.com/css2?family=Merienda:wght@400&display=swap">
<style>
  :root {
    --sand-light: #c9c9c9;
    --sand-mid: #a9a9a9;
    --sand-dark: #8f8f8f;
    --wet-sand: #d9d9d9;
    --sea: #bdbdbd;
    --ink: #141414;
    --shadow: rgba(0, 0, 0, 0.22);
  }
  html, body {
    margin: 0;
    padding: 0;
    overflow: hidden;
    background: var(--sand-mid);
  }
  .canvas {
    position: relative;
    width: 1200px;
    height: 1000px;
    overflow: hidden;
  }
  .beach-scene {
    position: absolute;
    inset: 0;
    background:
      linear-gradient(160deg, var(--sea) 0%, var(--wet-sand) 10%, var(--wet-sand) 22%, transparent 34%),
      linear-gradient(180deg, var(--sand-light) 0%, var(--sand-mid) 55%, var(--sand-dark) 100%);
  }
  .verse {
    position: absolute;
    inset: 0;
    margin: 0;
  }
  .verse-line {
    position: absolute;
    margin: 0;
    white-space: nowrap;
    line-height: 1;
    font-family: "Merienda", cursive;
    font-weight: 400;
    color: var(--ink);
    transform-origin: 0 50%;
    text-shadow: 0 26px 9px var(--shadow);
  }
  .verse-line--title   { left: 710px; top: 208px; font-size: 15px; transform: rotate(13deg); }
  .verse-line--long-1  { left: 443px; top: 196px; font-size: 17.5px; transform: rotate(12.2deg); }
  .verse-line--long-2  { left: 420px; top: 236px; font-size: 18px; transform: rotate(13.2deg); }
  .verse-line--long-3  { left: 375px; top: 276px; font-size: 18.5px; transform: rotate(13.8deg); }
  .verse-line--question-1 { left: 483px; top: 356px; font-size: 24px; transform: rotate(15.4deg); }
  .verse-line--question-2 { left: 458px; top: 416px; font-size: 24px; transform: rotate(16.6deg); }
  .verse-line--refrain { left: 470px; top: 496px; font-size: 28px; transform: rotate(19.4deg); }
  .verse-line--about   { left: 435px; top: 571px; font-size: 28px; transform: rotate(21.8deg); }
  .verse-line--closing { left: 235px; top: 609px; font-size: 33px; transform: rotate(20.8deg); }
</style>
</head>
<body>
  <main class="canvas">
    <div class="beach-scene" role="img" aria-label="Black and white photo of a sandy beach with the sea's edge at top left and a single pink rose lying on the sand near the bottom"></div>
    <section class="verse">
      <p class="verse-line verse-line--title">Marriage isn’t for you.</p>
      <p class="verse-line verse-line--long-1">You don’t marry to make yourself happy, you marry to make someone else happy.</p>
      <p class="verse-line verse-line--long-2">More than that, your marriage isn’t for yourself, you’re marrying for a family.</p>
      <p class="verse-line verse-line--long-3">Not just for the in-laws and all of that nonsense, but for your future children.</p>
      <p class="verse-line verse-line--question-1">Who do you want to help you raise them?</p>
      <p class="verse-line verse-line--question-2">Who do you want to influence them?</p>
      <p class="verse-line verse-line--refrain">Marriage isn’t for you.</p>
      <p class="verse-line verse-line--about">It’s not about you.</p>
      <p class="verse-line verse-line--closing">Marriage is about the person you married.</p>
    </section>
  </main>
</body>
</html>
```